Northfield Builders Guild Business card

We are looking for a new business card design with photo included.
Our business is a nonprofit construction contractor membership organization. We offer business education, assist with business setup and licensing, provide safety training, and provide a member directory.
URL: www.brickwayguildnetwork.org
Color code:
CMYK: 0 cyan, 42 magenta, 100 yellow, 0 black for Print.
Hexidecimal: #FF9900
RGB: R 255; G 153; B 0

```html
<!DOCTYPE html>
<html lang="en">
<head>
<meta charset="utf-8">
<title>Northfield Builders Guild — Business Card</title>
<link href="https://fonts.googleapis.com/css2?family=Montserrat:wght@400;500;700;800;900&display=swap" rel="stylesheet">
<style>
  :root {
    --orange: #ff9900;
    --charcoal: #363435;
    --ink: #2e2c2d;
    --paper: #ffffff;
    --mute: #9a9899;
    --stage: #2a2b2e;
    --photo-a: #3d5a6e;
    --photo-b: #5c7386;
  }
  * { box-sizing: border-box; margin: 0; padding: 0; }
  html, body { width: 1200px; height: 919px; overflow: hidden; }
  body {
    background: var(--stage);
    font-family: "Montserrat", Arial, sans-serif;
    position: relative;
  }
  .card {
    position: absolute;
    left: 250px;
    width: 700px;
    height: 400px;
    background: var(--paper);
    overflow: hidden;
  }
  .card--back { top: 40px; }
  .card--front { top: 479px; }

  /* Back side */
  .back-panel {
    position: absolute;
    inset: 24px 0 24px 34px;
    background: var(--charcoal);
  }
  .back-url {
    position: absolute;
    left: 26px;
    bottom: 14px;
    transform-origin: left bottom;
    transform: rotate(-90deg) translateY(100%);
    color: var(--paper);
    font-size: 15px;
    font-weight: 500;
    letter-spacing: 0.5px;
    white-space: nowrap;
  }
  .services {
    position: absolute;
    right: 34px;
    top: 56px;
    list-style: none;
    text-align: right;
  }
  .service {
    font-weight: 900;
    text-transform: uppercase;
    font-size: 26px;
    line-height: 0.95;
    letter-spacing: 1px;
    margin-bottom: 22px;
  }
  .service__lead { display: block; color: var(--paper); }
  .service__rest { display: block; color: var(--mute); }
  .service--grey .service__lead { color: var(--mute); }

  /* Front side */
  .photo {
    position: absolute;
    left: 34px;
    top: 40px;
    width: 320px;
    height: 336px;
    background: linear-gradient(135deg, var(--photo-b), var(--photo-a));
  }
  .info-panel {
    position: absolute;
    left: 354px;
    right: 0;
    top: 24px;
    bottom: 24px;
    background: var(--orange);
  }
  .brand {
    position: absolute;
    left: 18px;
    bottom: 44px;
    width: 222px;
    padding: 16px 18px;
    background: var(--charcoal);
    color: var(--paper);
    font-weight: 800;
    font-size: 22px;
    line-height: 1.05;
    text-transform: uppercase;
    letter-spacing: 0.5px;
  }
  .contact {
    position: absolute;
    right: 28px;
    bottom: 52px;
    text-align: right;
    color: var(--ink);
  }
  .contact__name {
    font-weight: 800;
    font-size: 34px;
    letter-spacing: 1px;
    text-transform: uppercase;
    line-height: 1;
  }
  .contact__role {
    font-size: 17px;
    font-weight: 500;
    margin-top: 4px;
  }
  .contact__rule {
    display: block;
    margin: 10px 0 10px auto;
    width: 110px;
    height: 2px;
    background: var(--ink);
  }
  .contact__line { font-size: 16px; font-weight: 500; line-height: 1.4; }
  .contact__line strong { font-weight: 700; }
</style>
</head>
<body>
  <section class="card card--back" aria-label="Business card back">
    <div class="back-panel">
      <p class="back-url">www.brickwayguildnetwork.org</p>
      <ul class="services">
        <li class="service"><span class="service__lead">Technical</span><span class="service__rest">Assistance</span></li>
        <li class="service"><span class="service__lead">Safety</span><span class="service__rest">&amp; Compliance</span></li>
        <li class="service service--grey"><span class="service__lead">Contractor</span><span class="service__rest">Directory</span></li>
        <li class="service"><span class="service__lead">Contractor</span><span class="service__lead">Education</span></li>
      </ul>
    </div>
  </section>

  <section class="card card--front" aria-label="Business card front">
    <div class="photo" role="img" aria-label="Photo of a construction worker in a yellow hard hat and safety vest looking upward"></div>
    <div class="info-panel"></div>
    <div class="brand">Northfield Builders Guild</div>
    <div class="contact">
      <p class="contact__name">Daniel Reyes</p>
      <p class="contact__role">construction contractor</p>
      <span class="contact__rule"></span>
      <p class="contact__line">Email; <strong>dreyes@nfbguild.org</strong></p>
      <p class="contact__line">Call; <strong>(555) 318-2047</strong></p>
    </div>
  </section>
</body>
</html>
```